Book Cover Design Project

Hello,

I am looking to get a cover created for my book.

Size 6 X 9

Title:
Quiet Ledger Steady Gains

Sub-Title:
Plain Methods for Growing Steady Gains Within Your Quiet Ledger

Author:
Martin Fenwick

The book could have an image or only typography.

If it does include an image do not use an image of a real person. If you use a person, he can be shaded in, outlined, etc

I like the color white and blue however, I am open to other colors as well.

Below is the cover of my previous book that has an image:
http://www.quillmarket.example/Dawn-Of-Stag-Path-Vowed-Final/dp/284610375K/ref=sr_1_1?ie=UTF8&s=books&qid=2417307529&sr=1-1

I like simple designs but open to other concepts also

attached is the text to be used for the back of the book.

Thank you in advance for your designs,

Target Market(s)

This book will be for small business owners. Typically males/females between the age of 25 - 45 looking to make more money without going broke with marketing.

Industry/Entity Type

Business

Requirements
Must have
• Must include the Title, Subtitle and Author on the cover

Nice to have
• An image that represents a small business growing
Should not have
• Images of a real person. Stylized versions are ok.

```html
<!DOCTYPE html>
<html lang="en">
<head>
<meta charset="utf-8">
<title>Quiet Ledger Steady Gains – Book Cover</title>
<link rel="stylesheet" href="https://fonts.googleapis.com/css2?family=PT+Sans:wght@400;700&family=Questrial&display=swap">
<style>
  :root {
    --brand-blue: #1570b8;
    --deep-blue: #0b4f8e;
    --navy: #083a66;
    --sky: #dce7f2;
    --band-grey: #a3a3a5;
    --quote-grey: #8c8c8c;
    --ink: #231f20;
    --paper: #ffffff;
  }
  * { margin: 0; padding: 0; box-sizing: border-box; }
  html, body { width: 1200px; height: 882px; overflow: hidden; background: var(--paper); }
  .cover {
    position: relative;
    width: 1200px;
    height: 882px;
    background: var(--paper);
    font-family: "PT Sans", Arial, sans-serif;
    color: var(--ink);
  }
  .edge-band { position: absolute; left: 0; width: 1200px; height: 30px; }
  .edge-band--top { top: 0; }
  .edge-band--bottom { bottom: 0; }

  /* Back cover */
  .back-copy {
    position: absolute;
    left: 52px;
    top: 44px;
    width: 560px;
  }
  .pull-quote {
    position: relative;
    font-family: "Questrial", "Century Gothic", sans-serif;
    font-size: 28px;
    line-height: 34px;
    color: var(--brand-blue);
    text-align: center;
    width: 500px;
    padding-top: 38px;
    padding-left: 8px;
  }
  .pull-quote__mark {
    position: absolute;
    font-family: Georgia, serif;
    font-size: 130px;
    line-height: 1;
    color: var(--quote-grey);
    font-weight: 700;
  }
  .pull-quote__mark--open { left: -12px; top: -6px; }
  .pull-quote__mark--close { left: 432px; top: 112px; }
  .section-heading {
    font-family: "Questrial", "Century Gothic", sans-serif;
    font-weight: 400;
    font-size: 20px;
    color: var(--brand-blue);
    margin-top: 26px;
    margin-bottom: 14px;
  }
  .body-text {
    font-size: 14.5px;
    line-height: 21px;
  }
  .body-text + .body-text { margin-top: 18px; }
  .benefit-list { list-style: none; font-size: 14.5px; line-height: 20px; }
  .benefit-list li { position: relative; padding-left: 28px; }
  .benefit-list li::before { content: "•"; position: absolute; left: 2px; }
  .benefit-list + .body-text { margin-top: 20px; }
  .author-site {
    font-family: "Questrial", "Century Gothic", sans-serif;
    font-size: 19px;
    color: var(--brand-blue);
    margin-top: 2px;
  }

  /* Front cover */
  .growth-illustration {
    position: absolute;
    left: 618px;
    top: 44px;
    width: 570px;
    height: 572px;
    border-radius: 28px 28px 0 0;
    background:
      linear-gradient(180deg, rgba(255,255,255,0) 78%, var(--paper) 100%),
      linear-gradient(160deg, var(--sky) 0%, #9fbddb 30%, var(--brand-blue) 55%, var(--deep-blue) 75%, var(--navy) 100%);
  }
  .title-block {
    position: absolute;
    left: 612px;
    top: 623px;
    width: 588px;
    height: 139px;
    background: var(--brand-blue);
    color: var(--paper);
    font-family: "Questrial", "Century Gothic", sans-serif;
    font-weight: 400;
    text-transform: uppercase;
  }
  .title-block__line1 {
    position: absolute; left: 50px; top: 14px;
    font-size: 46px; letter-spacing: 1px; line-height: 1;
  }
  .title-block__line2 {
    position: absolute; right: 24px; top: 62px;
    font-size: 66px; line-height: 1;
  }
  .subtitle-band {
    position: absolute;
    left: 612px;
    top: 762px;
    width: 588px;
    height: 38px;
    background: var(--band-grey);
    color: var(--ink);
    font-size: 14.5px;
    line-height: 38px;
    text-align: center;
  }
  .byline {
    position: absolute;
    left: 993px;
    top: 818px;
    font-size: 15px;
    color: var(--brand-blue);
  }
  .byline strong { font-weight: 700; }
</style>
</head>
<body>
<main class="cover">
  <svg class="edge-band edge-band--top" viewBox="0 0 1200 30" preserveAspectRatio="none" aria-hidden="true">
    <polygon points="0,0 715,0 760,30 0,30" fill="var(--brand-blue)"/>
    <polygon points="740,0 1200,0 1200,30 785,30" fill="var(--band-grey)"/>
  </svg>

  <section class="back-copy">
    <blockquote class="pull-quote">
      <span class="pull-quote__mark pull-quote__mark--open">“</span>
      Dramatically increase your<br>Sales and revenue with effective<br>Marketing Strategies,<br>Guaranteed to get results!
      <span class="pull-quote__mark pull-quote__mark--close">”</span>
    </blockquote>

    <h2 class="section-heading">Are lackluster sales getting you down?</h2>
    <p class="body-text">Does it seem like -- no matter how much testing and tweaking you do --<br>you continue to struggle with getting new customers, creating a strong<br>online and offline presence, and maximizing the lifetime value of existing<br>customers, and now you’re running out of time, patience... and money?</p>

    <h2 class="section-heading">What if I told you that I could help you:</h2>
    <ul class="benefit-list">
      <li>Gain and retain new customers</li>
      <li>Get others to promote your business</li>
      <li>Make more money from your existing customers</li>
      <li>Get results that will blow your competition away</li>
    </ul>
    <p class="body-text">... And I can show you how to do it FASTER, for a small fraction of what<br>you’d pay in-house marketing employees to get the SAME results!</p>
    <p class="body-text">Curious? Then open this book right now and I’ll explain how it’s done…</p>

    <h2 class="section-heading">About the Author:</h2>
    <p class="body-text">Martin Fenwick is a partner of Lumen Reach Marketing, which helps small<br>businesses get more customers by making them findable on the Internet.<br>He is a best selling author and has a bachelor’s degree in Internet<br>Marketing. He dedicates his time to learning as much as possible,<br>both in marketing and in life.</p>
    <p class="body-text">See how he can serve your business by going to</p>
    <p class="author-site">www.lumenreach.example</p>
  </section>

  <div class="growth-illustration" role="img" aria-label="Rising blue arrow over two world-map panels with a row of business silhouettes celebrating growth"></div>

  <h1 class="title-block">
    <span class="title-block__line1">Quiet Ledger</span>
    <span class="title-block__line2">Steady Gains</span>
  </h1>
  <p class="subtitle-band">Plain Methods for Growing Steady Gains Within Your Quiet Ledger</p>
  <p class="byline">By: <strong>Martin Fenwick</strong></p>

  <svg class="edge-band edge-band--bottom" viewBox="0 0 1200 30" preserveAspectRatio="none" aria-hidden="true">
    <polygon points="0,0 430,0 470,30 0,30" fill="var(--band-grey)"/>
    <polygon points="450,0 1200,0 1200,30 490,30" fill="var(--brand-blue)"/>
  </svg>
</main>
</body>
</html>
```